Demolition Company Billboard Design 13 feet wide 15 feet high

This is my first billboard on a busy road. I want it to be professional but with some eye catching flair that matches by business which is a demoltion business and also list my services. My company slogan is also

"call quill to clear the hill"

Target Market(s)

Home Ownerd and General Construction Companies

Industry/Entity Type

construction

Colors
0054AA
0677BA
7BADD7
CADEEF
E8F1F8

Requirements
Must have
• My services listed in the pictures my website and my phone number

```html
<!DOCTYPE html>
<html lang="en">
<head>
<meta charset="utf-8">
<title>Quill Hill Demolition Billboard</title>
<link href="https://fonts.googleapis.com/css2?family=Anton&family=Oswald:wght@400;500;600&display=swap" rel="stylesheet">
<style>
  :root {
    --page-bg: #f7f7f7;
    --white: #ffffff;
    --sky: #8e9597;
    --brick-dark: #2e2622;
    --brick-mid: #4a3a33;
    --accent-yellow: #fccc00;
    --band-teal: #3d84a6;
    --band-blue: #2a5a98;
    --band-navy: #233f85;
  }
  * { margin: 0; padding: 0; box-sizing: border-box; }
  html, body {
    width: 1200px;
    height: 1200px;
    overflow: hidden;
    background: var(--page-bg);
  }
  .billboard {
    position: absolute;
    left: 184px;
    top: 120px;
    width: 831px;
    height: 959px;
    overflow: hidden;
    color: var(--white);
  }
  .billboard__photo {
    position: absolute;
    inset: 0;
    background:
      radial-gradient(ellipse 45% 40% at 68% 62%, rgba(190,120,45,0.55), rgba(190,120,45,0) 70%),
      linear-gradient(180deg, var(--sky) 0%, #6f7475 14%, var(--brick-mid) 22%, var(--brick-dark) 60%, #221d1b 100%);
  }
  .billboard__band {
    position: absolute;
    inset: 0;
    width: 831px;
    height: 959px;
  }
  .brand-name {
    position: absolute;
    top: 137px;
    left: 0;
    width: 100%;
    text-align: center;
    font-family: "Oswald", sans-serif;
    font-weight: 400;
    font-size: 62px;
    line-height: 1;
    letter-spacing: 3px;
    transform: translateY(-50%);
  }
  .slogan {
    position: absolute;
    top: 261px;
    left: 0;
    width: 100%;
    text-align: center;
    font-family: "Anton", sans-serif;
    font-weight: 400;
    font-size: 120px;
    line-height: 150px;
    text-transform: uppercase;
    white-space: nowrap;
  }
  .services {
    position: absolute;
    top: 604px;
    left: 0;
    width: 100%;
    list-style: none;
    display: flex;
    justify-content: center;
    align-items: center;
    gap: 16px;
    font-family: "Oswald", sans-serif;
    font-weight: 400;
    font-size: 50px;
    line-height: 1;
    text-transform: uppercase;
    white-space: nowrap;
  }
  .services__item { display: flex; align-items: center; gap: 12px; }
  .services__item::before {
    content: "";
    width: 17px;
    height: 17px;
    border-radius: 50%;
    background: var(--white);
  }
  .contact {
    position: absolute;
    top: 852px;
    left: 0;
    width: 100%;
    height: 60px;
    font-family: "Oswald", sans-serif;
  }
  .contact__web {
    position: absolute;
    left: 53px;
    top: 0;
    height: 60px;
    display: flex;
    align-items: center;
    gap: 12px;
    font-size: 33px;
    font-weight: 500;
    white-space: nowrap;
  }
  .contact__phone {
    position: absolute;
    left: 425px;
    top: 0;
    height: 60px;
    display: flex;
    align-items: center;
    gap: 14px;
    font-size: 58px;
    font-weight: 600;
    letter-spacing: -1px;
    white-space: nowrap;
  }
  .icon { display: block; flex: none; fill: none; stroke: var(--white); }
</style>
</head>
<body>
  <main class="billboard">
    <div class="billboard__photo" role="img" aria-label="Photo of an orange excavator parked in front of a derelict brick factory under a grey overcast sky"></div>

    <svg class="billboard__band" viewBox="0 0 831 959" aria-hidden="true">
      <defs>
        <linearGradient id="bandGradient" x1="0" y1="0" x2="0.3" y2="1">
          <stop offset="0" stop-color="#3d84a6"/>
          <stop offset="0.55" stop-color="#2a5a98"/>
          <stop offset="1" stop-color="#233f85"/>
        </linearGradient>
      </defs>
      <polygon points="0,827 157,691 831,823 831,959 0,959" fill="#fccc00"/>
      <polygon points="0,845 157,723 831,841 831,959 0,959" fill="url(#bandGradient)"/>
    </svg>

    <div class="brand-name">QHD</div>

    <h1 class="slogan">“Call Quill To<br>Clear The Hill”</h1>

    <ul class="services">
      <li class="services__item">Interior</li>
      <li class="services__item">Exterior</li>
      <li class="services__item">Commercial</li>
    </ul>

    <div class="contact">
      <div class="contact__web">
        <svg class="icon" width="50" height="50" viewBox="0 0 52 52" stroke-width="4">
          <circle cx="26" cy="26" r="23"/>
          <ellipse cx="26" cy="26" rx="10" ry="23"/>
          <line x1="26" y1="3" x2="26" y2="49"/>
          <line x1="3" y1="26" x2="49" y2="26"/>
          <path d="M7 14 H45 M7 38 H45"/>
        </svg>
        <span>www.qhdemolition.com</span>
      </div>
      <div class="contact__phone">
        <svg class="icon" width="53" height="52" viewBox="0 0 56 54" stroke-width="3.5" stroke-linejoin="round" stroke-linecap="round">
          <path d="M12 4 L20 4 L24 16 L18 21 C21 30 26 35 34 38 L39 32 L51 36 L51 44 C51 48 48 51 44 50 C22 47 7 32 4 12 C4 7 7 4 12 4 Z"/>
          <path d="M32 14 A10 10 0 0 1 41 23"/>
          <path d="M33 5 A19 19 0 0 1 50 22"/>
        </svg>
        <span>555-014-2290</span>
      </div>
    </div>
  </main>
</body>
</html>
```